Bridgeway, Lantern, and the Quiet Harbor Loop Research Program Website

Overview: This website will serve a new research program (Bridgeway, Lantern, and the Quiet Harbor Loop) at the Fenmoor University School of Medicine. I want a clean, intuitive design that has a navigation bar, but uses icons/graphic buttons to link to the main pages. In an attached Word document, I have provided a basic information architecture for the site, understanding that this project would just generate graphics and code for the 3 pages. I highlighted the 3 pages I'd like designed.
Target market: People who want to participate in our research, or contribute grant funding to specific projects.
Number of page: The design project focuses on 3 pages, but the site must accommodate 6 pages with top-level links. See attached Word doc.
Logo and website header: Please integrate our logo in the header. I've uploaded it as a png file--both with the name of the website and with just the logo image. I imaging the logo would look great in a banner set against an image of a mountain. The two main design themes I want to see included are nature and healthcare.
Text content: I have not yet provided text. Use some dummy text.
Technical Specifications:
- Build using WordPress. We will host this site ourselves on Brimloft using WordPress.
- The design package must be coded.
- The template must be responsive to different platforms (e.g., computer, mobile phone, iPad).
Thank you! I look forward to seeing your designs.
- Ned

```html
<!DOCTYPE html>
<html lang="en">
<head>
<meta charset="utf-8">
<title>Bridgeway, Lantern, and the Quiet Harbor Loop – Research Program</title>
<link href="https://fonts.googleapis.com/css2?family=Baloo+2:wght@600;700;800&family=Poppins:wght@400;500;600&display=swap" rel="stylesheet">
<style>
:root{
  --blue:#1b5a94;
  --green:#4a9a3a;
  --green-soft:#e3eee0;
  --mist:#f0f5ee;
  --teal:#14a08a;
  --teal-dark:#108c78;
  --teal-mid:#20b49a;
  --teal-light:#79d8c8;
  --sky:#1d6fc0;
  --ink:#2c2c2c;
  --muted:#6b6b6b;
  --field:#f4f4f4;
  --grad:linear-gradient(90deg,var(--blue),var(--green));
}
*{box-sizing:border-box;margin:0;padding:0}
html,body{width:1200px;height:3594px;overflow:hidden}
body{position:relative;font-family:"Poppins",sans-serif;color:var(--ink);background:#fff}
.abs{position:absolute}
.center{left:0;width:1200px;text-align:center}
.heading{font-family:"Baloo 2",sans-serif;font-weight:800;font-size:36px;line-height:1;color:var(--blue)}
.heading span{color:var(--green)}
.sprig{display:block;margin:4px auto 0}
.btn{position:absolute;display:flex;align-items:center;justify-content:center;background:var(--grad);color:#fff;font-size:13px;border-radius:2px}

/* nav */
.nav{top:0;left:0;width:1200px;height:57px;background:rgba(240,246,252,.95);z-index:2}
.nav a{position:absolute;top:8px;width:120px;margin-left:-60px;text-align:center;font-size:13px;color:#333;text-decoration:none}
.nav a svg{display:block;margin:0 auto 3px}
.nav a.active{color:var(--sky)}
.nav a.active::after{content:"";display:block;width:38px;height:2px;background:var(--sky);margin:4px auto 0}

/* hero */
.hero{top:0;left:0;width:1200px;height:597px;background:linear-gradient(180deg,#c9d9e6 0%,#a9bfd0 30%,#7f96a8 55%,#6d6a66 80%,#5b4a40 100%)}
.hero-mark{top:96px;left:538px}
.hero-title{top:217px;font-family:"Baloo 2",sans-serif;font-weight:800;font-size:38px;color:var(--blue)}
.hero-sub{top:259px;font-family:"Baloo 2",sans-serif;font-weight:700;font-size:31px;color:var(--green)}
.hero-text{top:305px;font-size:23px;line-height:36px;color:#222}

/* vision */
.vision{top:597px;left:0;width:1200px;height:801px;background:var(--green-soft)}
.vision-text{top:141px;left:220px;width:760px;font-size:14.5px;line-height:23px;text-align:center;color:#333}
.card{position:absolute;top:272px;width:274px;height:373px;background:#fff;border-radius:10px;box-shadow:0 0 0 4px #f4f8f2,0 4px 10px rgba(0,0,0,.12)}
.card .photo{position:absolute;top:7px;left:7px;width:260px;height:180px;border-radius:4px}
.card .badge{position:absolute;top:147px;left:100px;width:74px;height:74px;border-radius:50%;background:radial-gradient(circle,#2f9a5a,#1f6e4a);border:4px solid #fff;display:flex;align-items:center;justify-content:center}
.card h3{position:absolute;top:238px;left:0;width:100%;text-align:center;font-size:15px;font-weight:600}
.card p{position:absolute;top:267px;left:14px;right:14px;text-align:center;font-size:14px;line-height:23px}

/* pillars */
.pillars{top:1398px;left:0;width:1200px;height:655px;background:#fff}
.pillar-title{font-size:20px;font-weight:500;color:#333}
.pillar-text{font-size:11px;line-height:19px;color:var(--muted)}
.know{font-size:15px;font-weight:500;color:var(--green)}

/* projects */
.projects{top:2053px;left:0;width:1200px;height:584px;background:var(--mist)}
.proj{position:absolute;top:203px;width:200px;height:261px;border-radius:8px}
.proj .cap{position:absolute;left:0;width:100%;text-align:center;color:#fff}
.proj .cap b{display:block;font-size:16px;font-weight:600}
.proj .cap small{font-size:12px}
.plus{position:absolute;bottom:-14px;left:86px;width:28px;height:28px;border-radius:50%;background:#fff;box-shadow:0 1px 4px rgba(0,0,0,.3);display:flex;align-items:center;justify-content:center}
.arrow{position:absolute;top:314px;width:36px;height:36px;border-radius:50%;border:1.5px solid #333;display:flex;align-items:center;justify-content:center;background:#fff}

/* contact */
.contact{top:2637px;left:0;width:1200px;height:593px;background:#fff}
.field{position:absolute;height:46px;background:var(--field);display:flex;align-items:center;font-size:12px;color:#444}
.field .ico{width:42px;height:100%;display:flex;align-items:center;justify-content:center;border-right:1px solid #e2e2e2;margin-right:12px}

/* footer */
.footer{top:3230px;left:0;width:1200px;height:364px;background:var(--teal);color:#fff}
.foot-h{font-size:18px;font-weight:500;letter-spacing:.3px}
.foot-h::after{content:"";display:block;width:26px;height:2px;background:#fff;margin-top:6px}
.foot-link{position:absolute;font-size:13px}
.social{position:absolute;top:246px;width:22px;height:22px;border-radius:50%;background:#fff;opacity:.9}
.copy{position:absolute;bottom:0;left:0;width:1200px;height:56px;background:var(--teal-dark);text-align:center;line-height:56px;font-size:13px}
</style>
</head>
<body>

<nav class="nav abs">
  <a class="active" style="left:264px"><svg width="16" height="16" viewBox="0 0 16 16" fill="none" stroke="currentColor" stroke-width="1.3"><path d="M2 7 8 2l6 5v7H2z"/><path d="M6 14v-4h4v4"/></svg>Home</a>
  <a style="left:389px"><svg width="18" height="16" viewBox="0 0 18 16" fill="none" stroke="var(--sky)" stroke-width="1.3"><circle cx="6" cy="5" r="3"/><circle cx="12" cy="5" r="3"/><path d="M1 14c0-3 2-5 5-5s5 2 5 5M10 9c3 0 6 2 6 5"/></svg>People</a>
  <a style="left:515px"><svg width="16" height="16" viewBox="0 0 16 16" fill="none" stroke="var(--sky)" stroke-width="1.3"><rect x="2" y="3" width="10" height="11" rx="1"/><path d="M7 10 14 2"/></svg>Projects</a>
  <a style="left:640px"><svg width="16" height="16" viewBox="0 0 16 16" fill="none" stroke="var(--sky)" stroke-width="1.3"><circle cx="8" cy="8" r="6"/><circle cx="8" cy="8" r="2.5"/></svg>Resources</a>
  <a style="left:766px"><svg width="16" height="16" viewBox="0 0 16 16" fill="none" stroke="var(--sky)" stroke-width="1.3"><circle cx="8" cy="8" r="6"/><path d="M6.3 6.5a1.8 1.8 0 1 1 2.4 1.7c-.5.2-.7.6-.7 1.1M8 11.2v.3"/></svg>FAQs</a>
  <a style="left:890px"><svg width="16" height="16" viewBox="0 0 16 16" fill="none" stroke="var(--sky)" stroke-width="1.3"><path d="M3 2h3l1 3-2 1c1 2 2 3 4 4l1-2 3 1v3c0 1-1 2-2 2C6 14 2 10 2 4c0-1 0-2 1-2z"/></svg>Contact Us</a>
</nav>

<header class="hero abs" role="img" aria-label="Misty mountain valley landscape at dawn">
  <svg class="hero-mark abs" width="124" height="118" viewBox="0 0 124 118" role="img" aria-label="Program emblem">
    <circle cx="62" cy="59" r="54" fill="#fff" opacity=".35"/>
  </svg>
  <div class="hero-title abs center">Bridgeway, Lantern, and the Quiet Harbor Loop</div>
  <div class="hero-sub abs center">The Research Program</div>
  <p class="hero-text abs center">Lorem Ipsum Dolor Sit Amet, Consectetur Adipiscing Elit,<br>Sed Do Eiusmod Tempor Incididunt Ut Labore</p>
  <div class="btn" style="top:428px;left:525px;width:139px;height:38px">Contact Us</div>
</header>

<section class="vision abs">
  <div class="abs center" style="top:68px">
    <h2 class="heading">Our <span>Vision</span></h2>
    <svg class="sprig" width="30" height="14" viewBox="0 0 30 14" fill="none" stroke="var(--green)" stroke-width="1.2"><path d="M4 12c4-1 7-4 11-10M15 12c-2-4-1-7 1-9M15 12c4 0 8-3 11-8"/></svg>
  </div>
  <p class="vision-text abs">Lorem ipsum dolor sit amet, consectetur adipiscing elit, sed do eiusmod tempor incididunt ut labore et dolore magna aliqua. Ut enim ad minim veniam,&nbsp; quis nostrud exercitation ullamco laboris. Lorem ipsum dolor sit amet, magna aliqua. Ut enim ad minim veniam,&nbsp; quis nostrud exercitation ullamco laboris</p>

  <article class="card" style="left:160px">
    <div class="photo" role="img" aria-label="Colleagues working together at a laptop" style="background:linear-gradient(135deg,#6d5a4a,#b9a48a,#3f3a36)"></div>
    <div class="badge"><svg width="40" height="30" viewBox="0 0 40 30" fill="none" stroke="#fff" stroke-width="1.4"><circle cx="20" cy="8" r="4"/><circle cx="9" cy="11" r="3.5"/><circle cx="31" cy="11" r="3.5"/><path d="M12 26c0-5 4-9 8-9s8 4 8 9M2 26c0-4 3-7 7-7M38 26c0-4-3-7-7-7"/></svg></div>
    <h3>PEOPLE</h3>
    <p>Lorem Ipsum Dolor Sit Amet, Consectetur Adipiscing Elit, Sed Do Labore Et Dolore Magna</p>
  </article>
  <article class="card" style="left:463px">
    <div class="photo" role="img" aria-label="Scientists at microscopes in a laboratory" style="background:linear-gradient(135deg,#d8dde0,#9aa4aa,#e7eaec)"></div>
    <div class="badge"><svg width="32" height="34" viewBox="0 0 32 34" fill="none" stroke="#fff" stroke-width="1.4"><rect x="4" y="5" width="20" height="26" rx="2"/><path d="M10 3h8v4h-8zM8 14h6M8 19h8M8 24h6M20 14l3 3 6-6"/></svg></div>
    <h3>PROJECTS</h3>
    <p>Lorem Ipsum Dolor Sit Amet, Consectetur Adipiscing Elit, Sed Do Labore Et Dolore Magna</p>
  </article>
  <article class="card" style="left:764px">
    <div class="photo" role="img" aria-label="Thoughtful man in front of a chalkboard covered in question marks" style="background:linear-gradient(135deg,#2d302c,#4b4e48,#1f211e)"></div>
    <div class="badge"><svg width="36" height="32" viewBox="0 0 36 32" fill="none" stroke="#fff" stroke-width="1.4"><rect x="2" y="12" width="18" height="14" rx="2"/><path d="M6 26v4l4-4M6 17h10M6 21h8"/><circle cx="25" cy="11" r="8"/><path d="M23 9a2 2 0 1 1 2.5 2c-.4.2-.5.5-.5 1M25 14v.3"/></svg></div>
    <h3>FAQ'S</h3>
    <p>Lorem Ipsum Dolor Sit Amet, Consectetur Adipiscing Elit, Sed Do Labore Et Dolore Magna</p>
  </article>

  <div class="btn" style="top:682px;left:530px;width:140px;height:39px">Read More</div>
</section>

<section class="pillars abs">
  <div class="abs center" style="top:70px">
    <h2 class="heading">Our <span>Three Pillars</span></h2>
    <svg class="sprig" width="30" height="14" viewBox="0 0 30 14" fill="none" stroke="var(--green)" stroke-width="1.2"><path d="M4 12c4-1 7-4 11-10M15 12c-2-4-1-7 1-9M15 12c4 0 8-3 11-8"/></svg>
  </div>
  <p class="abs center" style="top:148px;font-size:14px;line-height:23px;color:#333">Lorem Ipsum Dolor Sit Amet, Consectetur Adipiscing Elit, Sed Do Eiusmod<br>Tempor Incididunt Ut Labore Et Dolore.</p>

  <div class="abs center" style="top:212px">
    <div class="pillar-title">Values</div>
    <p class="pillar-text" style="margin-top:4px">Lorem Ipsum Dolor Sit Amet, Consectetur Adipiscing Elit, Sed<br>Do Eiusmod Tempor Incididunt Ut Labore Et Dolore Magna</p>
    <div class="know" style="margin-top:6px">Know More</div>
  </div>

  <div class="abs" style="top:440px;left:160px;width:274px;text-align:right">
    <div class="pillar-title">Health care</div>
    <p class="pillar-text" style="margin-top:4px">Lorem Ipsum Dolor Sit Amet, Consectetur Adipiscing Elit, Sed Do Eiusmod Tempor Incididunt Ut Labore Et Dolore Magna</p>
    <div class="know" style="margin-top:2px">Know More</div>
  </div>
  <div class="abs" style="top:442px;left:766px;width:250px">
    <div class="pillar-title">Spiritual Life</div>
    <p class="pillar-text" style="margin-top:4px">Lorem Ipsum Dolor Sit Amet, Consectetur Adipiscing Elit, Sed Do Eiusmod Tempor Incididunt Ut Labore Et Dolore Magna</p>
    <div class="know" style="margin-top:2px">Know More</div>
  </div>

  <svg class="abs" style="top:320px;left:455px" width="290" height="270" viewBox="0 0 290 270">
    <circle cx="145" cy="82" r="81" fill="#1f6fbf"/>
    <circle cx="202" cy="176" r="81" fill="var(--teal-light)"/>
    <circle cx="88" cy="176" r="81" fill="var(--teal-mid)" opacity=".95"/>
    <path d="M145 82m-81 0" fill="none"/>
    <circle cx="145" cy="140" r="39" fill="#fff"/>
    <circle cx="145" cy="140" r="26" fill="none" stroke="var(--green)" stroke-width="2"/>
    <g fill="none" stroke="#fff" stroke-width="2">
      <path d="M128 50h22l7 9-18 20-18-20z"/><path d="M121 59h36M134 50l5 9-0 20M144 50l-5 9"/>
      <circle cx="158" cy="40" r="9"/>
      <path d="M88 200c-14-10-24-18-24-28 0-7 5-11 11-11 6 0 10 4 13 8 3-4 7-8 13-8 6 0 11 4 11 11"/>
      <path d="M66 180h8l4-6 5 12 4-6h6"/><circle cx="104" cy="188" r="7"/><path d="M104 184v8M100 188h8"/>
      <path d="M211 160l22 38h-44z"/><circle cx="211" cy="184" r="5"/><path d="M199 184c6-8 18-8 24 0c-6 8-18 8-24 0"/>
    </g>
  </svg>
</section>

<section class="projects abs">
  <div class="abs center" style="top:72px">
    <h2 class="heading">Our <span>Projects</span></h2>
    <svg class="sprig" width="30" height="14" viewBox="0 0 30 14" fill="none" stroke="var(--green)" stroke-width="1.2"><path d="M4 12c4-1 7-4 11-10M15 12c-2-4-1-7 1-9M15 12c4 0 8-3 11-8"/></svg>
  </div>
  <p class="abs center" style="top:144px;font-size:14px;color:#333">Lorem Ipsum Dolor Sit Amet, Consectetur Adipiscing Elit, Sed Do</p>

  <div class="arrow" style="left:84px"><svg width="10" height="10" viewBox="0 0 10 10" fill="none" stroke="#333" stroke-width="1.6"><path d="M6.5 1.5 3 5l3.5 3.5"/></svg></div>
  <div class="arrow" style="left:1076px"><svg width="10" height="10" viewBox="0 0 10 10" fill="none" stroke="#333" stroke-width="1.6"><path d="M3.5 1.5 7 5 3.5 8.5"/></svg></div>

  <div class="proj" style="left:160px;background:linear-gradient(160deg,#2b79c0,#4a95d6 45%,#2b3a4e)" role="img" aria-label="Researchers examining a sample in a lab">
    <div class="cap" style="top:196px"><b>Project 1</b><small>Lorem Ipsum Dolor Sit Amet</small></div>
    <div class="plus"><svg width="12" height="12" viewBox="0 0 12 12" stroke="#111" stroke-width="2.2"><path d="M6 1v10M1 6h10"/></svg></div>
  </div>
  <div class="proj" style="left:386px;background:linear-gradient(160deg,#6aaa3a,#5a9a30);box-shadow:inset 0 0 0 5px #b9a48a" role="img" aria-label="Doctor with a patient, shown under a green highlight">
    <div class="cap" style="top:126px"><b>Project 2</b><small>Lorem Ipsum Dolor Sit Amet</small></div>
    <div class="plus" style="bottom:auto;top:178px"><svg width="12" height="12" viewBox="0 0 12 12" stroke="#111" stroke-width="2.2"><path d="M6 1v10M1 6h10"/></svg></div>
  </div>
  <div class="proj" style="left:612px;background:linear-gradient(160deg,#5a5650,#2f2c29 60%,#1a1a1a)" role="img" aria-label="Two colleagues in conversation">
    <div class="cap" style="top:196px"><b>Project 3</b><small>Lorem Ipsum Dolor Sit Amet</small></div>
    <div class="plus"><svg width="12" height="12" viewBox="0 0 12 12" stroke="#111" stroke-width="2.2"><path d="M6 1v10M1 6h10"/></svg></div>
  </div>
  <div class="proj" style="left:838px;background:linear-gradient(160deg,#cfd3d6,#7f868c 50%,#2c3440)" role="img" aria-label="Business colleagues reviewing notes">
    <div class="cap" style="top:196px"><b>Project 4</b><small>Lorem Ipsum Dolor Sit Amet</small></div>
    <div class="plus"><svg width="12" height="12" viewBox="0 0 12 12" stroke="#111" stroke-width="2.2"><path d="M6 1v10M1 6h10"/></svg></div>
  </div>
</section>

<section class="contact abs">
  <div class="abs center" style="top:70px">
    <h2 class="heading">Our <span>Projects</span></h2>
    <svg class="sprig" width="30" height="14" viewBox="0 0 30 14" fill="none" stroke="var(--green)" stroke-width="1.2"><path d="M4 12c4-1 7-4 11-10M15 12c-2-4-1-7 1-9M15 12c4 0 8-3 11-8"/></svg>
  </div>
  <p class="abs center" style="top:136px;font-size:14px;color:#333">Lorem Ipsum Dolor Sit Amet, Consectetur Adipiscing Elit, Sed Do</p>

  <div class="field" style="top:196px;left:240px;width:343px"><span class="ico"><svg width="12" height="12" viewBox="0 0 12 12" fill="#aaa"><circle cx="6" cy="3.5" r="3"/><path d="M0 12c0-4 3-5 6-5s6 1 6 5z"/></svg></span>Your Name*</div>
  <div class="field" style="top:196px;left:610px;width:343px"><span class="ico"><svg width="10" height="13" viewBox="0 0 10 13" fill="none" stroke="#aaa" stroke-width="1.3"><path d="M5 12s4-4 4-7a4 4 0 0 0-8 0c0 3 4 7 4 7z"/><circle cx="5" cy="5" r="1.3"/></svg></span>Email*</div>
  <div class="field" style="top:254px;left:240px;width:343px"><span class="ico"><svg width="12" height="12" viewBox="0 0 12 12" fill="#aaa"><path d="M2 0h2l1 3-1.5 1c.8 1.6 2 2.8 3.5 3.5L8 6l3 1v2c0 1-1 2-2 2C4 11 0 7 0 2 0 1 1 0 2 0z"/></svg></span>Phone*</div>
  <div class="field" style="top:254px;left:610px;width:343px"><span class="ico"><svg width="13" height="12" viewBox="0 0 13 12" fill="none" stroke="#aaa" stroke-width="1.2"><rect x="1" y="2" width="8" height="9"/><path d="M5 8l7-7"/></svg></span>Inquiry For*</div>
  <div class="field" style="top:316px;left:240px;width:711px;height:109px;align-items:flex-start;padding-top:14px"><span class="ico" style="height:20px;border:0"><svg width="13" height="13" viewBox="0 0 13 13" fill="none" stroke="#aaa" stroke-width="1.1"><circle cx="6.5" cy="6.5" r="5.5"/><path d="M5 5a1.5 1.5 0 1 1 2 1.4c-.4.2-.5.5-.5.9M6.5 9.2v.3"/></svg></span>How can we help you?</div>

  <div class="btn" style="top:474px;left:530px;width:140px;height:39px">Submit Now</div>
</section>

<footer class="footer abs">
  <div class="abs" style="top:90px;left:160px;display:flex;align-items:center">
    <span style="width:44px;height:44px;border-radius:50%;border:2px solid #fff;display:block"></span>
    <span style="width:1px;height:40px;background:#fff;margin:0 8px;display:block"></span>
    <span style="font-size:11px;font-weight:600;line-height:14px">Bridgeway, Lantern, and the Quiet Harbor Loop<br>The Research Program</span>
  </div>
  <p class="abs" style="top:156px;left:160px;width:310px;font-size:11px;line-height:19px">Lorem Ipsum Dolor Sit Amet, Consectetur Adipiscing Elit, Sed Do Eiusmod Tempor Incididunt Ut Labore Et Dolore Magna</p>
  <span class="social" style="left:160px"></span>
  <span class="social" style="left:198px"></span>
  <span class="social" style="left:236px"></span>
  <span class="social" style="left:274px"></span>

  <div class="abs foot-h" style="top:84px;left:547px">QUICK LINKS</div>
  <span class="foot-link" style="top:128px;left:548px">Home</span>
  <span class="foot-link" style="top:163px;left:548px">Our Vision</span>
  <span class="foot-link" style="top:201px;left:548px">People</span>
  <span class="foot-link" style="top:241px;left:548px">Projects</span>
  <span class="foot-link" style="top:128px;left:651px">Resources</span>
  <span class="foot-link" style="top:163px;left:651px">FAQs</span>
  <span class="foot-link" style="top:203px;left:651px">Contact Us</span>

  <div class="abs foot-h" style="top:84px;left:809px">CONTACT DETAILS</div>
  <svg class="abs" style="top:130px;left:809px" width="11" height="14" viewBox="0 0 11 14" fill="#fff"><path d="M5.5 14S0 8.5 0 5.5a5.5 5.5 0 0 1 11 0C11 8.5 5.5 14 5.5 14zm0-6.5a2 2 0 1 0 0-4 2 2 0 0 0 0 4z"/></svg>
  <span class="foot-link" style="top:128px;left:836px;line-height:20px">48, Alder Row, Fenmoor,<br>State</span>
  <svg class="abs" style="top:194px;left:809px" width="12" height="12" viewBox="0 0 12 12" fill="#fff"><path d="M2 0h2l1 3-1.5 1c.8 1.6 2 2.8 3.5 3.5L8 6l3 1v2c0 1-1 2-2 2C4 11 0 7 0 2 0 1 1 0 2 0z"/></svg>
  <span class="foot-link" style="top:191px;left:836px">555-014-2286</span>
  <svg class="abs" style="top:246px;left:808px" width="14" height="10" viewBox="0 0 14 10" fill="none" stroke="#fff" stroke-width="1.4"><rect x="1" y="1" width="12" height="8"/><path d="M1 1l6 5 6-5"/></svg>
  <span class="foot-link" style="top:241px;left:836px">hello@blqresearchloop.org</span>

  <div class="copy">Copyright © 2021 BLQ Research Program. All Rights Reserved.</div>
</footer>

</body>
</html>
```